Criação de Papelaria (6 itens) para Beleza
" Somos uma Distribuidora de Cosméticos. Compramos os produtos diretamente das Indústrias e depois revendemos para lojistas em MG e no Norte do Rio. Antes, nós éramos uma distribuidora apenas da marca Vorani (https://www.voranicosmeticos.com.br/). Por esse motivo, utilizávamos uma logo feita pelo marketing deles, nas cores deles, para que as duas logos sempre andassem casadas. Hoje, ampliamos o nosso mix e distribuímos também os produtos da Mirtex ( https://www.mirtex.com.br/) e da henna Sol de Jade. Ou seja, hoje somos efetivamente uma distribuidora de Cosméticos em geral, atendendo os michos de cabelo, pele, maquiagem e unhas. Dessa maneira, criamos uma nova logo, para representar a Distribuidora. "

```html
<!DOCTYPE html>
<html lang="pt-BR">
<head>
<meta charset="utf-8">
<title>Quintela – Cartão de visita</title>
<link href="https://fonts.googleapis.com/css2?family=Montserrat:wght@400;500&display=swap" rel="stylesheet">
<style>
  :root {
    --page: #e6e6e8;
    --navy: #243240;
    --navy-deep: #1a2430;
    --gold: #c9a85a;
    --gold-light: #e8d08f;
    --paper: #ffffff;
    --paper-shade: #eeeeef;
    --ink: #2a2f36;
    --ink-soft: #4a4f57;
    --brand-text: #ecebe8;
  }
  * { box-sizing: border-box; margin: 0; padding: 0; }
  html, body {
    width: 1200px; height: 1200px; overflow: hidden;
    background: var(--page);
    font-family: "Montserrat", sans-serif;
  }
  .canvas {
    width: 1200px; height: 1200px;
    display: flex; align-items: center; justify-content: center;
  }
  .card {
    position: relative;
    width: 1100px; height: 240px;
    background: linear-gradient(160deg, var(--navy) 0%, var(--navy-deep) 100%);
    border-radius: 34px 48px 0 34px;
    overflow: hidden;
  }
  .card__base-line {
    position: absolute; left: 384px; right: 0; bottom: 5px;
    height: 3px;
    background: linear-gradient(90deg, var(--gold), var(--gold-light), var(--gold));
  }
  .brand {
    position: absolute; left: 0; top: 0; width: 376px; height: 240px;
    display: flex; align-items: center; justify-content: center;
  }
  .brand__name {
    font-weight: 400; font-size: 40px;
    color: var(--brand-text); line-height: 1;
  }
  .panel {
    position: absolute; left: 384px; right: 0; top: 0; bottom: 18px;
    background: linear-gradient(180deg, var(--paper) 0%, var(--paper) 70%, var(--paper-shade) 100%);
    border-left: 8px solid var(--gold);
    border-radius: 40px 48px 0 0;
  }
  .panel__gold-edge {
    position: absolute; left: 376px; top: 14px; bottom: 18px; width: 3px;
    background: linear-gradient(180deg, var(--gold-light), var(--gold));
  }
  .holder {
    position: absolute; left: 47px; top: 36px;
    font-weight: 500; font-size: 30px; color: var(--ink);
  }
  .contact {
    position: absolute; left: 66px; top: 98px;
    display: flex; flex-direction: column; gap: 8px;
  }
  .contact__row {
    display: flex; align-items: center; gap: 14px;
    font-size: 21px; color: var(--ink-soft); line-height: 1.1;
  }
  .contact__phones { display: flex; flex-direction: column; }
  .contact__row--mail { margin-top: 10px; }
  .icon { width: 24px; height: 24px; flex: none; }
  .address {
    position: absolute; left: 388px; top: 112px;
    display: flex; align-items: flex-start; gap: 14px;
    font-size: 21px; color: var(--ink-soft); line-height: 1.2;
  }
  .address .icon { margin-top: 6px; }
</style>
</head>
<body>
<main class="canvas">
  <article class="card">
    <div class="brand">
      <span class="brand__name">Quintela</span>
    </div>
    <span class="panel__gold-edge"></span>
    <section class="panel">
      <h1 class="holder">Lívia Teixeira Moura Alves</h1>
      <div class="contact">
        <div class="contact__row">
          <svg class="icon" viewBox="0 0 24 24" aria-hidden="true">
            <circle cx="12" cy="12" r="10.5" fill="none" stroke="#2a2f36" stroke-width="1.6"/>
            <path d="M9 7.5c.6 0 1 .9 1.3 1.8.2.6-.6 1-.6 1.4.3 1 1.6 2.4 2.6 2.8.4 0 .8-.8 1.4-.6.9.3 1.8.8 1.8 1.3 0 .9-1 1.8-2 1.8-3 0-6.3-3.3-6.3-6.3 0-1 .9-2.2 1.8-2.2z" fill="#2a2f36"/>
          </svg>
          <div class="contact__phones">
            <span>(22) 2614 0275</span>
            <span>(22) 99172-4608</span>
          </div>
        </div>
        <div class="contact__row contact__row--mail">
          <svg class="icon" viewBox="0 0 24 24" aria-hidden="true">
            <circle cx="12" cy="12" r="10.5" fill="none" stroke="#2a2f36" stroke-width="1.6"/>
            <rect x="6.5" y="8" width="11" height="8" rx="1" fill="none" stroke="#2a2f36" stroke-width="1.4"/>
            <path d="M6.8 8.5l5.2 4 5.2-4" fill="none" stroke="#2a2f36" stroke-width="1.4"/>
          </svg>
          <span>lumiaromas@mailvia.com</span>
        </div>
      </div>
      <div class="address">
        <svg class="icon" viewBox="0 0 24 24" aria-hidden="true">
          <circle cx="12" cy="12" r="10.5" fill="none" stroke="#2a2f36" stroke-width="1.8"/>
          <path d="M12 5.5a4.3 4.3 0 0 0-4.3 4.3c0 3.2 4.3 8.2 4.3 8.2s4.3-5 4.3-8.2A4.3 4.3 0 0 0 12 5.5z" fill="#2a2f36"/>
          <circle cx="12" cy="9.8" r="1.6" fill="#ffffff"/>
        </svg>
        <p>Av. Ernesto Lobato - 415<br>Cavaleiros - Macaé - RJ<br>CEP 27920-150</p>
      </div>
    </section>
    <span class="card__base-line"></span>
  </article>
</main>
</body>
</html>
```